Business Card Design Project

I am a Chiropractor that is looking for a new business card.  Our logo was slightly changed lately, therefore need a new, more professional look.
We are a modern, non-stuffy chiropractic office.  Want a contemporary look that will let people know this is not your typical doctors office.  Our logo is red, and contains the name of our business: realign.  The u in the logo is green, stressing the most important part of our business: "u"

Target Market(s)
moderate to upper income bracket, family friendly
www.realignspine.example
Gordon Pell
Family Chiropractor
412 Birch Ave
Cedarton, TX 78699
512.555.0147 phone
512.555.0148 fax
Industry/Entity Type
Business
Requirements
Must have
- www.realignspine.example
Gordon Pell
Family Chiropractor
412 Birch Ave
Cedarton, TX 78699
512.555.0147 phone
512.555.0148 fax

```html
<!DOCTYPE html>
<html lang="en">
<head>
<meta charset="utf-8">
<title>realign business card</title>
<link rel="stylesheet" href="https://fonts.googleapis.com/css2?family=Open+Sans:wght@400;600;700&display=swap">
<style>
  :root {
    --backdrop: #3b2414;
    --card: #ffffff;
    --brand-red: #ee3f37;
    --brand-green: #6ab545;
    --ink: #3d3d3d;
    --ink-soft: #555555;
    --rule: #8a8a8a;
  }
  * { margin: 0; padding: 0; box-sizing: border-box; }
  html, body {
    width: 1200px; height: 412px; overflow: hidden;
    background: var(--backdrop);
    font-family: "Open Sans", Arial, sans-serif;
  }
  .sheet { position: relative; width: 1200px; height: 412px; }
  .card {
    position: absolute; top: 64px;
    width: 497px; height: 284px;
    background: var(--card);
    box-shadow: 0 4px 14px rgba(0,0,0,0.45);
    overflow: hidden;
  }
  .card--front { left: 76px; }
  .card--back { left: 627px; }

  .brand-name {
    position: absolute; left: 0; right: 0;
    text-align: center; font-weight: 400;
    line-height: 1; letter-spacing: 1px;
  }
  .card--front .brand-name { top: 62px; font-size: 50px; color: var(--brand-red); }
  .card--back .brand-name { top: 82px; font-size: 88px; color: var(--brand-green); }

  .identity {
    position: absolute; left: 0; right: 0; top: 176px;
    text-align: center; color: var(--ink);
    font-size: 13px;
  }
  .identity__name { font-weight: 700; font-size: 15.5px; }
  .identity__title { color: var(--ink-soft); }

  .contact {
    position: absolute; top: 216px; left: 0; width: 100%;
    font-size: 12.5px; line-height: 17px; color: var(--ink-soft);
  }
  .contact__address { position: absolute; right: 266px; text-align: right; white-space: nowrap; }
  .contact__rule {
    position: absolute; left: 253px; top: 4px;
    width: 1px; height: 26px; background: var(--rule);
  }
  .contact__phones { position: absolute; left: 275px; }
  .contact__line { display: flex; align-items: center; gap: 5px; white-space: nowrap; }
  .contact__icon { width: 10px; height: 10px; fill: var(--ink-soft); }

  .footer-band { position: absolute; left: 0; bottom: 0; width: 497px; height: 23px; }
  .footer-band__url {
    position: absolute; right: 20px; bottom: 4px;
    font-size: 11.5px; letter-spacing: 2.6px;
    color: #ffffff; white-space: nowrap;
  }
</style>
</head>
<body>
<main class="sheet">
  <section class="card card--front">
    <div class="brand-name">realign</div>

    <div class="identity">
      <span class="identity__name">Gordon Pell /</span>
      <span class="identity__title">Family Chiropractor</span>
    </div>

    <div class="contact">
      <div class="contact__address">412 Birch Ave<br>Cedarton, TX 78699</div>
      <div class="contact__rule"></div>
      <div class="contact__phones">
        <div class="contact__line">
          <svg class="contact__icon" viewBox="0 0 10 10" aria-hidden="true"><path d="M2 0.5 L3.6 2.6 L2.8 3.6 Q3.8 5.8 6.4 7.2 L7.4 6.4 L9.5 8 L8.3 9.5 Q2.8 8.6 0.5 1.7 Z"/></svg>
          <span>512.555.0147</span>
        </div>
        <div class="contact__line">
          <svg class="contact__icon" viewBox="0 0 10 10" aria-hidden="true"><path d="M0.5 3 Q5 0 9.5 3 L8.8 4.4 L7 3.8 L7 3 Q5 2.2 3 3 L3 3.8 L1.2 4.4 Z M2.2 5 H7.8 L9 9.5 H1 Z"/></svg>
          <span>512.555.0148</span>
        </div>
      </div>
    </div>

    <svg class="footer-band" viewBox="0 0 497 23" aria-hidden="true">
      <polygon points="0,0 268,0 245,23 0,23" fill="var(--brand-green)"/>
      <polygon points="281,0 497,0 497,23 258,23" fill="var(--brand-red)"/>
    </svg>
    <div class="footer-band__url">www.realignspine.example</div>
  </section>

  <section class="card card--back">
    <div class="brand-name">realign</div>
    <svg class="footer-band" viewBox="0 0 497 23" aria-hidden="true">
      <polygon points="0,0 268,0 245,23 0,23" fill="var(--brand-green)"/>
      <polygon points="281,0 497,0 497,23 258,23" fill="var(--brand-red)"/>
    </svg>
    <div class="footer-band__url">www.realignspine.example</div>
  </section>
</main>
</body>
</html>
```